Pactwise - Training I Consulting I Review - Related to Contracts/Agreements

We provide legal services, we need a plattform to book video online trainings or local trainings classes and appointments (with calendar feature to select date and see availability at screen), payment over internet, legal document creation over webpage, videos will be produces in the next 3 - 4 moths so this is a place holder item. Participants for the Online trainings shall have a login in area with secured password. Appointments for local trainings and Consulting. Consider Outline in file attached. I can send you also a video with more explanation regarding the purpose.

Target Market(s)

Startup/scale up Software companies that intent to have an international business and need help with their contracts, to sell their products. Sales persons.

Industry/Entity Type

Legal

Coding

Coded - Design and coding required

Number of Pages Required

5+ page

Font styles to use
Serif
Sans Serif

Colors
000000
eeeeee
f5f5f5
ffffff
f8fcfd
3277b5
ecf7fb
cadf82
86cfc6

Requirements
Must have
• See file pactwise attached with outline. Moreover see here first starting point: https://moritz-ebbing.sitebuildr-demo.net/mysite-1 . Main inspiration comes from www.advisoryhub-demo.net from the log in area, see the outline in the file attached with the screen shots. At the end I need someone who can draft the full webpage and maintain it for a yearly fee. It must be simple and well structured layout. Lean. 1st landing page shall not scroll, 2 landing page only a little to see the testimonials and foster of page. There should be a Progress Bar to indicate the booking/selection process. Calendar booking. Easy fast booking.
• I like the colour mix, the feeling and the easy structor of:
• https://www.artpitch-demo.net/design/6374387or
• https://www.artpitch-demo.net/design/6372391 or https://www.artpitch-demo.net/design/6374366
• https://www.agencyfind-demo.net/en/web-design/belgium-be
• https://www.artpitch-demo.net/design/5896857
• https://www.artpitch-demo.net/design/5902173
• https://www.artpitch-demo.net/design/17197349
• https://www.artpitch-demo.net/design/5464461
• https://www.artpitch-demo.net/design/7180908
Nice to have
• page for evaluation and interview, see outline attached in the file with screen shots. Document upload.
Should not have
• many pictures, long scroll down pages on the 1st and 2nd ladding pages, many colours and forms. No need for news letter, search field, no need for links to Chatterly and other social media (except workNet).

```html
<!DOCTYPE html>
<html lang="en">
<head>
<meta charset="utf-8">
<title>Pactwise – Our Policy</title>
<link rel="stylesheet" href="https://fonts.googleapis.com/css2?family=Mulish:wght@400;600;700&family=Libre+Baskerville&display=swap">
<style>
  :root {
    --header-dark: #3a3a3c;
    --header-mid: #4a4a4d;
    --page-bg: #f5f5f5;
    --ink: #222325;
    --body-text: #7b8088;
    --accent: #7fd0ea;
    --accent-deep: #5fbfdf;
    --accent-text: #6cc6e6;
    --tab-dark: #3b3b3d;
    --tab-light: #5a5a5c;
    --white: #ffffff;
    --rule: #6a6a6c;
  }
  * { box-sizing: border-box; margin: 0; padding: 0; }
  html, body { width: 1200px; height: 628px; overflow: hidden; }
  body {
    position: relative;
    background: var(--page-bg);
    font-family: "Mulish", "Helvetica Neue", Arial, sans-serif;
    color: var(--ink);
  }

  /* Header */
  .site-header {
    position: absolute; left: 0; top: 0; width: 1200px; height: 64px;
  }
  .header-texture, .footer-texture {
    position: absolute; inset: 0;
    background: linear-gradient(120deg, #2f2f31 0%, #4b4b4e 35%, #3a3a3c 60%, #525255 100%);
  }
  .brand {
    position: absolute; left: 79px; top: 0; height: 64px;
    display: flex; align-items: center; gap: 14px;
  }
  .brand-square {
    width: 30px; height: 30px; border: 2px solid var(--white);
  }
  .brand-name {
    font-family: "Libre Baskerville", Georgia, serif;
    font-size: 27px; color: var(--white); letter-spacing: 0.3px;
  }
  .main-nav {
    position: absolute; top: 0; height: 64px; left: 0; width: 1200px;
  }
  .nav-item {
    position: absolute; top: 23px; font-size: 15px; color: var(--white);
    display: flex; align-items: center; gap: 6px; white-space: nowrap;
  }
  .nav-item.refer { left: 594px; }
  .nav-item.services { left: 793px; color: var(--accent-text); }
  .nav-item.partner { left: 918px; }
  .nav-underline {
    position: absolute; left: 786px; top: 61px; width: 72px; height: 3px;
    background: var(--accent);
  }
  .login-button {
    position: absolute; left: 1007px; top: 16px; width: 112px; height: 33px;
    background: linear-gradient(#93daf0, var(--accent-deep));
    border-radius: 2px; box-shadow: 0 1px 3px rgba(0,0,0,.35);
    color: var(--white); font-size: 14px;
    display: flex; align-items: center; justify-content: center; gap: 5px;
  }

  /* Policy section */
  .policy {
    position: absolute; left: 0; top: 64px; width: 1200px; height: 420px;
  }
  .policy-title {
    position: absolute; top: 58px; width: 100%; text-align: center;
    font-size: 29px; font-weight: 400; color: var(--ink);
  }
  .policy-tabs {
    position: absolute; left: 156px; top: 124px; width: 888px; height: 33px;
    display: flex;
  }
  .tab {
    height: 33px; padding-left: 14px; display: flex; align-items: center;
    font-size: 15px; font-weight: 700; color: var(--white);
    background: linear-gradient(var(--tab-light), var(--tab-dark));
    border-left: 1px solid #8a8a8c; position: relative;
  }
  .tab.active {
    background: var(--accent); font-weight: 600; border-left: none;
  }
  .tab.active::after {
    content: ""; position: absolute; left: 22px; bottom: -6px;
    border-left: 6px solid transparent; border-right: 6px solid transparent;
    border-top: 6px solid var(--accent);
  }
  .tab.general { width: 280px; }
  .tab.privacy { width: 201px; }
  .tab.disclaimer { width: 203px; }
  .tab.webpage { width: 204px; }
  .policy-text {
    position: absolute; left: 156px; top: 184px; width: 888px;
    font-size: 12.6px; line-height: 19.2px; color: var(--body-text);
    text-align: justify;
  }
  .policy-list {
    position: absolute; top: 278px; list-style: none;
    font-size: 13px; color: var(--body-text);
  }
  .policy-list.first { left: 157px; }
  .policy-list.second { left: 359px; }
  .policy-list li {
    height: 24px; display: flex; align-items: center; gap: 7px;
  }

  /* Footer */
  .site-footer {
    position: absolute; left: 0; top: 484px; width: 1200px; height: 144px;
  }
  .footer-links {
    position: absolute; top: 28px; list-style: none;
    font-size: 15px; color: var(--white);
  }
  .footer-links li { height: 29px; }
  .footer-links.col-1 { left: 156px; }
  .footer-links.col-2 { left: 371px; }
  .footer-links.col-3 { left: 536px; top: 26px; }
  .footer-links.col-4 { left: 676px; top: 26px; }
  .appointment-button {
    position: absolute; left: 816px; top: 34px; width: 168px; height: 34px;
    background: linear-gradient(#93daf0, var(--accent-deep));
    box-shadow: 0 1px 3px rgba(0,0,0,.35);
    color: var(--white); font-size: 13px;
    display: flex; align-items: center; justify-content: center;
  }
  .social-link {
    position: absolute; left: 1005px; top: 32px;
    display: flex; align-items: center; gap: 6px;
    color: var(--white); font-size: 12px;
  }
  .social-circle {
    width: 38px; height: 38px; border-radius: 50%;
    background: #2a2a2c; box-shadow: 0 2px 4px rgba(0,0,0,.5);
  }
  .footer-rule {
    position: absolute; left: 132px; top: 104px; width: 936px; height: 1px;
    background: var(--rule);
  }
  .copyright {
    position: absolute; top: 116px; width: 100%; text-align: center;
    font-size: 13px; color: var(--white);
  }
  .copyright .brand-mention { color: var(--accent-text); }
</style>
</head>
<body>

<header class="site-header">
  <div class="header-texture" role="img" aria-label="Dark grey faceted background texture"></div>
  <div class="brand">
    <span class="brand-square"></span>
    <span class="brand-name">Pactwise</span>
  </div>
  <nav class="main-nav">
    <span class="nav-item refer">
      <svg width="15" height="13" viewBox="0 0 15 13" aria-hidden="true">
        <circle cx="5" cy="3.5" r="3" fill="#e0504a"/>
        <path d="M0 12.5c0-3.5 2.2-5 5-5s5 1.5 5 5z" fill="#e0504a"/>
        <circle cx="11" cy="4" r="2.5" fill="#e0504a"/>
        <path d="M9.5 8c1-.6 1.6-.7 2.2-.7 2 0 3.3 1.5 3.3 4.2h-4z" fill="#e0504a"/>
      </svg>
      Refere Someone
    </span>
    <span class="nav-item services">Services</span>
    <span class="nav-item partner">Partner</span>
    <span class="nav-underline"></span>
    <span class="login-button">
      <svg width="10" height="12" viewBox="0 0 10 12" aria-hidden="true">
        <circle cx="5" cy="3" r="3" fill="#fff"/>
        <path d="M0 12c0-3.5 2-5 5-5s5 1.5 5 5z" fill="#fff"/>
      </svg>
      Login
    </span>
  </nav>
</header>

<main class="policy">
  <h1 class="policy-title">Our Policy</h1>
  <div class="policy-tabs">
    <span class="tab general active">General Terms and Conditions</span>
    <span class="tab privacy">Privacy Policy</span>
    <span class="tab disclaimer">Disclaimer</span>
    <span class="tab webpage">Web Page Policy</span>
  </div>
  <p class="policy-text">Lorem Ipsum passage, and going through the cites of the word in classical literature, discovered the undoubtable source. Lorem Ipsum comes from sections 1.10.32 and 1.10.33 of "de Finibus Bonorum et Malorum" (The Extremes of Good and Evil) by Cicero Lorem ipsum dolor sit amet, consectetur adipiscing elit, sed do eiusmod tempor incididunt ut labore et dolore magna aliqua. Ut enim ad minim veniam, quis nostrud exercitation ullamco laboris nisi ut aliquip ex ea commodo consequat. Duis aute irure dolor in reprehenderit in voluptate velit esse cillum.</p>

  <ul class="policy-list first">
    <li><svg width="11" height="11" viewBox="0 0 11 11" aria-hidden="true"><rect x=".5" y=".5" width="10" height="10" fill="none" stroke="#7fd0ea"/><path d="M2.5 5.5l2 2 4-5" fill="none" stroke="#7fd0ea" stroke-width="1.4"/></svg>There are many page</li>
    <li><svg width="11" height="11" viewBox="0 0 11 11" aria-hidden="true"><rect x=".5" y=".5" width="10" height="10" fill="none" stroke="#7fd0ea"/><path d="M2.5 5.5l2 2 4-5" fill="none" stroke="#7fd0ea" stroke-width="1.4"/></svg>Lorem Ipsum available</li>
    <li><svg width="11" height="11" viewBox="0 0 11 11" aria-hidden="true"><rect x=".5" y=".5" width="10" height="10" fill="none" stroke="#7fd0ea"/><path d="M2.5 5.5l2 2 4-5" fill="none" stroke="#7fd0ea" stroke-width="1.4"/></svg>Contrary to popular</li>
  </ul>
  <ul class="policy-list second">
    <li><svg width="11" height="11" viewBox="0 0 11 11" aria-hidden="true"><rect x=".5" y=".5" width="10" height="10" fill="none" stroke="#7fd0ea"/><path d="M2.5 5.5l2 2 4-5" fill="none" stroke="#7fd0ea" stroke-width="1.4"/></svg>There are many page</li>
    <li><svg width="11" height="11" viewBox="0 0 11 11" aria-hidden="true"><rect x=".5" y=".5" width="10" height="10" fill="none" stroke="#7fd0ea"/><path d="M2.5 5.5l2 2 4-5" fill="none" stroke="#7fd0ea" stroke-width="1.4"/></svg>Slightly Believable.</li>
    <li><svg width="11" height="11" viewBox="0 0 11 11" aria-hidden="true"><rect x=".5" y=".5" width="10" height="10" fill="none" stroke="#7fd0ea"/><path d="M2.5 5.5l2 2 4-5" fill="none" stroke="#7fd0ea" stroke-width="1.4"/></svg>Lorem Ipsum available</li>
  </ul>
</main>

<footer class="site-footer">
  <div class="footer-texture" role="img" aria-label="Dark grey faceted background texture"></div>
  <ul class="footer-links col-1"><li>Evaluation</li><li>Market Feedback</li></ul>
  <ul class="footer-links col-2"><li>Students</li><li>Templates</li></ul>
  <ul class="footer-links col-3"><li>Policies</li><li>Tools</li></ul>
  <ul class="footer-links col-4"><li>Team</li><li>Contact</li></ul>
  <span class="appointment-button">Make an Appointment</span>
  <span class="social-link"><span class="social-circle"></span>workNet</span>
  <div class="footer-rule"></div>
  <p class="copyright">© 2018 <span class="brand-mention">Pactwise</span> All Right Reserved.</p>
</footer>

</body>
</html>
```